Morrow Engineering Core Values Branding Package

Morrow Engineering has recently refined its company Core Values and is seeking a strong, cohesive branding package to visually bring these values to life. The new graphic assets will communicate our commitment to excellence in a way that resonates with our team, clients, and partners in a blue-collar, industrial environment.

We are looking for multiple visual assets with consistent design elements that can be applied across platforms. The tone should reflect strength, reliability, and professionalism while remaining approachable and aligned with our industry.

Core Values & Descriptions
Accountability
“We take ownership of our work and actions, ensuring reliability and trust in every solution we deliver.”

Teamwork
“We collaborate across departments and disciplines to provide the highest level of service and innovation for our clients.”

Integrity
“We operate with honesty, transparency, and ethical standards in all aspects of our business.”

Growth
“We are committed to continuous improvement—of our people, our processes, and our impact in the industry.”

Deliverables

1. Primary Core Values Graphic
A master visual representing all four values together.
Designed for use on posters, office signage, internal presentations.

2. Individual Value Graphics (x4)
One graphic per core value: Accountability, Teamwork, Integrity, Growth.
Cohesive style with slight visual variation to reflect each value’s unique meaning.

Target Market(s)

Employees of Morrow Engineering

Industry/Entity Type

Blue Collar

Font styles to use
Sans Serif

Colors
0054AA
0677BA
7BADD7
CADEEF
E8F1F8
00AB8E
00BBA5
67D7C9
C6EFE9
E9F9F6
EB3D1F
EC4F4E
F09395
F8D3D4
FCEDEE

Requirements
Must have
• Accountability, Teamwork, Integrity, Growth

```html
<!DOCTYPE html>
<html lang="en">
<head>
<meta charset="utf-8">
<title>Morrow Engineering – Core Values</title>
<link rel="stylesheet" href="https://fonts.googleapis.com/css2?family=Lato:wght@400;700&family=Roboto:wght@900&display=swap">
<style>
  :root {
    --navy: #003a70;
    --green: #3dae2b;
    --green-bright: #22d10a;
    --gold: #e6ad45;
    --red: #c8102e;
    --ring: #c9c9c9;
    --ink: #111111;
    --paper: #ffffff;
  }
  * { margin: 0; padding: 0; box-sizing: border-box; }
  html, body { width: 954px; height: 1200px; overflow: hidden; background: var(--paper); }
  .poster { position: relative; width: 954px; height: 1200px; background: var(--paper); overflow: hidden; }

  .title {
    position: absolute; left: 0; width: 954px; top: 78px; text-align: center;
    font-family: "Roboto", sans-serif; font-weight: 900; font-size: 98px; line-height: 1;
    color: var(--navy); letter-spacing: -0.5px;
  }
  .website {
    position: absolute; left: 468px; top: 176px; width: 344px; text-align: right;
    font-family: "Lato", sans-serif; font-weight: 400; font-size: 16px;
    letter-spacing: 10px; color: var(--navy); white-space: nowrap;
  }

  .wave { position: absolute; left: 0; top: 240px; width: 954px; height: 210px; }

  .divider { position: absolute; background: var(--navy); }
  .divider--vertical { left: 473px; top: 290px; width: 5px; height: 910px; }
  .divider--horizontal { left: 0; top: 789px; width: 954px; height: 5px; }

  .hub { position: absolute; left: 326px; top: 642px; width: 300px; height: 300px; }
  .hub__name {
    position: absolute; left: 326px; width: 300px; top: 767px; text-align: center;
    font-family: "Roboto", sans-serif; font-weight: 900; font-size: 44px; line-height: 48px;
    color: var(--paper);
  }

  .value__title {
    position: absolute; white-space: nowrap;
    font-family: "Roboto", sans-serif; font-weight: 900; font-size: 43px; line-height: 44px;
    letter-spacing: -0.3px;
  }
  .value__icon { position: absolute; width: 86px; height: 86px; border-radius: 50%; }
  .value__text {
    position: absolute; white-space: nowrap;
    font-family: "Lato", sans-serif; font-weight: 700; font-size: 18px; line-height: 25.5px;
    color: var(--ink);
  }

  .value--accountability .value__title { left: 103px; top: 455px; color: var(--navy); }
  .value--teamwork .value__title { left: 529px; top: 455px; color: var(--gold); }
  .value--integrity .value__title { left: 103px; top: 947px; color: var(--red); }
  .value--growth .value__title { left: 529px; top: 947px; color: var(--green); }

  .value--accountability .value__icon { left: 47px; top: 540px; background: var(--navy); }
  .value--teamwork .value__icon { left: 537px; top: 540px; background: var(--gold); }
  .value--integrity .value__icon { left: 54px; top: 1026px; background: var(--red); }
  .value--growth .value__icon { left: 534px; top: 1026px; background: var(--green); }

  .value--accountability .value__text { left: 154px; top: 525px; }
  .value--teamwork .value__text { left: 646px; top: 525px; }
  .value--integrity .value__text { left: 154px; top: 1007px; }
  .value--growth .value__text { left: 646px; top: 1007px; }
</style>
</head>
<body>
<main class="poster">
  <h1 class="title">CORE VALUES</h1>
  <p class="website">www.morroweng.com</p>

  <svg class="wave" viewBox="0 240 954 210" aria-hidden="true">
    <path fill="var(--green-bright)" d="M0,366 C150,330 260,260 380,249 C520,240 650,290 760,330 C840,355 900,362 954,362 L954,392 C880,398 800,385 700,335 C600,290 500,283 400,283 C250,290 100,360 0,378 Z"/>
    <path fill="var(--green)" d="M0,398 C100,370 180,310 270,278 C340,254 400,249 450,253 C560,262 650,300 720,340 C800,388 880,412 954,408 L954,437 C860,447 790,422 700,372 C620,330 560,300 460,292 C380,286 330,298 290,318 C200,358 120,405 60,427 C30,438 10,440 0,438 Z"/>
  </svg>

  <div class="divider divider--vertical"></div>
  <div class="divider divider--horizontal"></div>

  <svg class="hub" viewBox="0 0 300 300" aria-hidden="true">
    <circle cx="150" cy="150" r="146" fill="none" stroke="var(--ring)" stroke-width="5"/>
    <circle cx="150" cy="150" r="136" fill="var(--paper)" stroke="var(--ring)" stroke-width="5"/>
    <circle cx="150" cy="150" r="118" fill="var(--navy)"/>
  </svg>
  <p class="hub__name">MORROW</p>

  <section class="value value--accountability">
    <h2 class="value__title">ACCOUNTABILITY</h2>
    <div class="value__icon" role="img" aria-label="Icon of a person reviewing a checklist"></div>
    <p class="value__text">We take ownership of our<br>work and actions, ensuring<br>reliability and trust in every<br>solution we deliver.</p>
  </section>

  <section class="value value--teamwork">
    <h2 class="value__title">TEAMWORK</h2>
    <div class="value__icon" role="img" aria-label="Icon of interlocking puzzle pieces"></div>
    <p class="value__text">We collaborate across<br>departments and<br>disciplines to provide the<br>highest level of service and<br>innovation for our clients.</p>
  </section>

  <section class="value value--integrity">
    <h2 class="value__title">INTEGRITY</h2>
    <div class="value__icon" role="img" aria-label="Icon of a hand holding a person with an award"></div>
    <p class="value__text">We operate with honesty,<br>transparency, and ethical<br>standards in all aspects of<br>our business.</p>
  </section>

  <section class="value value--growth">
    <h2 class="value__title">GROWTH</h2>
    <div class="value__icon" role="img" aria-label="Icon of a gear with a check mark and rising arrow"></div>
    <p class="value__text">We are committed to<br>continuous improvement—<br>of our people, our<br>processes, and our impact<br>in the industry.</p>
  </section>
</main>
</body>
</html>
```